Financial Consulting Company in need of technical diagram

Attached is a basic template to follow, however the following changes must be made:
- Get rid of reflection boxes at the bottom
-Delete anything in parentheses
-Change top box to read "Uncover Value Opportunities"
-Change bottom right box to read "Sales and Operations Planning"
-Change bottom left box to read "Financial Planning"

Additionally we would like to see something a little more creative and cohesive. One possibility is using "Cheveron" type arrows to show the "wheel" effect.

Please email tmorven@brightlake7.example if you have any questions!
Updates

Please see newly uploaded image for an example of how we would like it re-created.

Industry/Entity Type

Financial

Requirements
Must have
• I'm looking for something that keeps the "wheel" approach, but is not a direct re-creation of the example given. The boxes for example, dont' necessarily need to stay boxes. Feel free to play around with placement as well.
Nice to have
• Please see green wheel for example of how it can be re-created.

```html
<!DOCTYPE html>
<html lang="en">
<head>
<meta charset="utf-8">
<title>Value Cycle Diagram</title>
<link rel="stylesheet" href="https://fonts.googleapis.com/css2?family=Carlito:wght@700&display=swap">
<style>
  :root {
    --canvas-bg: #ffffff;
    --step-top: #6b97cc;
    --step-mid: #4a7bb7;
    --step-bottom: #3b67a0;
    --step-edge: #34608f;
    --step-text: #ffffff;
    --arrow-fill: #4f82bf;
    --shadow: rgba(40, 60, 90, 0.35);
  }
  * { box-sizing: border-box; margin: 0; padding: 0; }
  html, body {
    width: 1200px;
    height: 900px;
    overflow: hidden;
    background: var(--canvas-bg);
  }
  .cycle-diagram {
    position: relative;
    width: 1200px;
    height: 900px;
    font-family: "Carlito", "Calibri", sans-serif;
  }
  .cycle-arrows {
    position: absolute;
    inset: 0;
    width: 1200px;
    height: 900px;
  }
  .cycle-step {
    position: absolute;
    display: flex;
    align-items: center;
    justify-content: center;
    text-align: center;
    color: var(--step-text);
    font-weight: 700;
    font-size: 29px;
    line-height: 1.35;
    border-radius: 16px;
    border: 2px solid var(--step-edge);
    background:
      linear-gradient(180deg, rgba(255,255,255,0.28) 0%, rgba(255,255,255,0.06) 48%, rgba(255,255,255,0) 50%),
      linear-gradient(180deg, var(--step-top) 0%, var(--step-mid) 50%, var(--step-bottom) 100%);
    box-shadow: 4px 6px 8px var(--shadow), inset 0 -4px 8px rgba(0,0,0,0.15);
    text-shadow: 0 1px 2px rgba(0,0,0,0.3);
  }
  .step-uncover   { left: 450px; top: 114px; width: 320px; height: 122px; }
  .step-strategize{ left: 762px; top: 282px; width: 280px; height: 128px; }
  .step-sales     { left: 642px; top: 572px; width: 318px; height: 148px; }
  .step-financial { left: 262px; top: 572px; width: 310px; height: 118px; }
  .step-assess    { left: 172px; top: 282px; width: 276px; height: 128px; }
</style>
</head>
<body>
<main class="cycle-diagram">
  <svg class="cycle-arrows" viewBox="0 0 1200 900" aria-hidden="true">
    <defs>
      <marker id="arrow-head" viewBox="0 0 10 10" refX="5" refY="5" markerWidth="3.6" markerHeight="3.6" orient="auto-start-reverse">
        <path d="M0,0 L10,5 L0,10 L2.5,5 Z" fill="var(--arrow-fill)"/>
      </marker>
    </defs>
    <g fill="none" stroke="var(--arrow-fill)" stroke-width="9" stroke-linecap="round" marker-end="url(#arrow-head)">
      <path class="arrow-uncover-strategize" d="M784,196 Q826,212 846,252"/>
      <path class="arrow-strategize-sales" d="M930,444 Q938,500 906,538"/>
      <path class="arrow-sales-financial" d="M628,704 Q608,700 590,706"/>
      <path class="arrow-financial-assess" d="M316,548 Q292,512 296,468"/>
      <path class="arrow-assess-uncover" d="M368,262 Q392,234 428,222"/>
    </g>
  </svg>

  <div class="cycle-step step-uncover">Uncover Value<br>Opportunities</div>
  <div class="cycle-step step-strategize">Strategize<br>and Align</div>
  <div class="cycle-step step-sales">Sales and<br>Operations<br>Planning</div>
  <div class="cycle-step step-financial">Financial<br>Planning</div>
  <div class="cycle-step step-assess">Assess the<br>Results</div>
</main>
</body>
</html>
```